High-end executive coaching group needs a 2 page digital flyer

We need a 2 page digital flyer for a high end leadership coaching offering for global leaders in healthcare. The flyer will advertise a new service (an elite senior leadership coaching group) for senior leaders in the healthcare industry from around the world.
The flyer should be upmarket, professional and minimalist in style to meet the expectations of my professional market (very senior doctors and executives).
The design should be based on my existing logo and brand, see my landing page: www.marlowadvisory.com
The key elements needed are
1) An editable PDF which we can update as we revise the specific details of the offering. The text and draft design for this is attached.
2) The banner image should be high quality but abstract. It can be based on the landing page of my website (the two ripple effects) but does not need to strictly adhere to this.
3) The logo placement of the Marlow Advisory delta sign should be discreet so that it does not dominate
4) The small logos of our professional accrediting organisations should be discreetly placed at the end and should not dominate. They might work best as mono icons in a footer (e.g. blue on a white background, or white on blue.
5) Please find enclosed a previous flyer as an example of a similar style we have used for more junior professionals. The design worked quite well, although we now need a more upmarket version for our senior executives.
Updates

Please note this design specifically needs to use existing branding and images from my website: marlowadvisory.com. We are definitely not looking for stock "leadership team" images for this high-end brochure.

Target Market(s)

Senior global leaders in the healthcare industry

Industry/Entity Type

Leading business schools & Healthcare industry.

Font styles to use
Other font styles liked:
• Operetta (selective use for heading) and Sofia Pro (body text)

Colors
0054AA
0677BA
7BADD7
CADEEF
E8F1F8

Requirements
Must have
• Clean minimalist and high professionally look that directly speaks to the interests and perspectives of senior leader leaders in healthcare. It also needs very clear call to action sections
Nice to have
• Effective presentation of the two bios and photographs. These need to look impressive, but should not dominate.
Should not have
• Loud and bold colours, large use of logos.

```html
<!DOCTYPE html>
<html lang="en">
<head>
<meta charset="utf-8">
<title>Marlow Advisory – Analytic Coaching Group for Senior Leaders</title>
<link rel="stylesheet" href="https://fonts.googleapis.com/css2?family=Gilda+Display&family=Mulish:wght@400;500;600&display=swap">
<style>
:root{
  --brand-deep:#0054AA;
  --brand-mid:#0677BA;
  --brand-soft:#7BADD7;
  --brand-pale:#CADEEF;
  --brand-mist:#E8F1F8;
  --panel:#dfe9f6;
  --ink:#2c3e66;
  --muted:#4a5a7c;
  --stage:#2a2a2a;
  --white:#ffffff;
}
*{box-sizing:border-box;margin:0;padding:0}
html,body{width:1200px;height:3027px;overflow:hidden}
body{background:var(--stage);font-family:"Mulish",sans-serif;color:var(--ink)}
.serif{font-family:"Gilda Display",serif;font-weight:400}
.page{position:absolute;left:154px;width:911px;background:var(--white);overflow:hidden}
.page-one{top:181px;height:1288px}
.page-two{top:1540px;height:1305px}
.abs{position:absolute}

/* page one */
.hero-art{left:0;top:0;width:911px;height:520px;
  background:radial-gradient(ellipse 300px 90px at 455px 200px,#9cc3e6 0%,#b9d5ee 40%,rgba(220,234,247,0) 100%),
  linear-gradient(180deg,#c3dbf1 0%,#d9e8f6 45%,#eef5fb 75%,#ffffff 100%)}
.headline{left:73px;top:354px;font-size:47px;color:var(--brand-deep);letter-spacing:.3px;white-space:nowrap}
.subline{left:74px;top:424px;font-size:22px;line-height:28px;color:var(--brand-mid);font-weight:400}
.intro-card{left:47px;top:535px;width:816px;height:141px;background:var(--white);z-index:1;
  box-shadow:0 1px 6px rgba(0,40,100,.15);padding:44px 0 0 31px;font-size:16px;line-height:20px;color:#1f2a44}
.section-band{left:0;top:506px;width:568px;height:50px;background:var(--brand-deep);z-index:2;
  clip-path:polygon(0 0,100% 0,94% 100%,0 100%);color:var(--white);font-size:22px;line-height:50px;padding-left:79px;white-space:nowrap}
.benefits{left:45px;top:699px;width:508px;height:362px;background:var(--panel);padding:18px 20px 0 22px}
.benefits h2{font-size:27px;color:var(--brand-deep);margin:0 0 6px 14px}
.benefits ul{list-style:none}
.benefits li{font-size:16px;line-height:20px;color:var(--muted);padding-left:14px;position:relative}
.benefits li::before{content:"";position:absolute;left:1px;top:8px;width:5px;height:5px;border-radius:50%;background:var(--brand-deep)}
.benefits li strong{display:block;color:var(--brand-deep);font-weight:500}
.quote-card{border:2px solid var(--brand-deep);background:var(--white);text-align:center}
.quote-mark{display:block;margin:0 auto}
.quote-text{font-size:16px;line-height:20px;color:var(--muted)}
.quote-name{font-size:16px;color:var(--brand-deep);font-weight:500}
.quote-one{left:578px;top:699px;width:288px;height:460px}
.quote-one .quote-mark{margin-top:40px}
.quote-one .quote-text{margin-top:42px;padding:0 26px}
.quote-one .quote-name{margin-top:20px}
.cta-block{position:absolute;left:0;bottom:0;width:100%;height:98px;background:var(--brand-deep);color:var(--white);
  font-size:19px;line-height:23px;padding-top:14px}
.date-bar{left:45px;top:1084px;width:508px;height:37px;background:var(--brand-deep);color:var(--white);
  text-align:center;font-size:18px;line-height:37px;letter-spacing:.3px}
.time-bar{left:45px;top:1124px;width:508px;height:36px;background:var(--panel);color:var(--brand-deep);
  text-align:center;font-size:18px;line-height:36px}
.details{left:67px;top:1175px;font-size:16px;line-height:20px;color:var(--muted)}
.details .label{color:var(--brand-deep);display:inline-block}
.brand-mark{display:flex;align-items:center;gap:12px}
.brand-mark .dot{width:30px;height:30px;border-radius:50%;background:var(--brand-deep);flex:none}
.brand-mark .name{font-family:"Mulish",sans-serif;font-weight:400;font-size:24px;line-height:25px;color:var(--brand-soft)}
.brand-one{left:620px;top:1200px}

/* page two */
.top-band{left:34px;top:33px;width:847px;height:43px;background:var(--brand-deep);color:var(--white);
  font-size:21px;line-height:43px;padding-left:32px;white-space:nowrap}
.bio-card{top:93px;width:411px;height:585px;border:2px solid var(--brand-mid);background:var(--white)}
.bio-left{left:36px}
.bio-right{left:470px}
.portrait-ring{position:absolute;left:112px;top:26px;width:184px;height:184px;border-radius:50%;background:var(--white);
  box-shadow:0 2px 8px rgba(0,40,100,.25);display:flex;align-items:center;justify-content:center}
.portrait{width:162px;height:162px;border-radius:50%}
.portrait-a{background:radial-gradient(circle at 50% 45%,#c9a58f 0%,#8aa36a 55%,#4d7a45 100%)}
.portrait-b{background:radial-gradient(circle at 50% 50%,#c49a86 0%,#6e3b2e 50%,#151515 100%)}
.bio-name{position:absolute;top:224px;width:100%;text-align:center;font-size:25px;color:var(--brand-deep)}
.bio-text{position:absolute;left:29px;right:29px;top:270px;font-size:16px;line-height:20.4px;color:var(--muted);
  text-align:justify}
.explore{left:64px;top:700px;width:800px;font-size:16px;line-height:20px;color:#1f2a44}
.explore ul{list-style:none;margin-top:22px}
.explore li{padding-left:14px;position:relative}
.explore li::before{content:"";position:absolute;left:1px;top:8px;width:5px;height:5px;border-radius:50%;background:var(--brand-deep)}
.spots{left:34px;top:829px;width:413px;height:236px;background:var(--panel)}
.spots .tag{position:absolute;left:26px;top:37px;width:369px;height:46px;background:var(--brand-deep);color:var(--white);
  text-align:center;font-size:21px;line-height:46px}
.spots .pitch{position:absolute;left:0;top:101px;width:100%;text-align:center;font-size:22px;line-height:26px;color:var(--brand-deep)}
.quote-two{left:470px;top:829px;width:411px;height:236px;border-width:1.5px}
.quote-two .quote-mark{margin-top:14px}
.quote-two .quote-text{margin-top:14px;padding:0 28px}
.quote-two .quote-name{margin-top:14px;color:#1f2a44;font-weight:400}
.brand-two{left:64px;top:1093px}
.accreditations{left:544px;top:1102px;display:flex;gap:18px;align-items:center}
.badge{background:var(--brand-deep);opacity:.85}
.badge-round{width:42px;height:42px;border-radius:50%}
.badge-square{width:72px;height:34px;border-radius:3px}
.footer{left:0;top:1185px;width:911px;height:120px}
.footer-art{position:absolute;left:0;top:0}
.footer-call{left:64px;top:1207px;font-size:32px;line-height:40px;color:var(--white)}
.contacts{left:578px;top:1209px;font-size:17px;line-height:22px;color:var(--brand-deep)}
.contacts .row{display:flex;align-items:center;gap:8px}
.contacts .site{font-size:21px;margin-top:14px;padding-left:25px}
</style>
</head>
<body>

<section class="page page-one">
  <div class="abs hero-art" role="img" aria-label="Abstract water droplet falling onto a pale blue rippled surface"></div>
  <h1 class="abs headline serif">Elevate and Ignite Your Leadership</h1>
  <p class="abs subline">Transformative conversations for senior healthcare leaders.<br>Unlock purpose, engage authentically and amplify your leadership impact.</p>

  <div class="abs intro-card">
    As a senior leader in healthcare, you’re constantly navigating challenges.<br>
    But where do you turn for authentic connections, reflection and personal growth?<br>
    Rethink your leadership assumptions and approach challenges with fresh creativity.<br>
    Secure your spot in our exclusive Analytic Coaching Group and ignite your leadership potential.
  </div>

  <div class="abs section-band">Analytic Coaching Group for Senior Leaders</div>

  <div class="abs benefits">
    <h2 class="serif">Benefits</h2>
    <ul>
      <li><strong>Transformative conversations:</strong>&nbsp;Engage in discussions that spark innovative leadership</li>
      <li><strong>Peer insights:</strong>Harness fresh insights from peers, enhancing your decision-making and effectiveness</li>
      <li><strong>Reimagined leadership:</strong>Channel your creativity and redefine your leadership, personally and professionally</li>
      <li><strong>Instant 360° insights:</strong>Gain real-time feedback from trusted peers to enrich your leadership</li>
      <li><strong>Lead authentically:</strong>Develop effective strategies using the latest insights from group and leadership psychology</li>
    </ul>
  </div>

  <div class="abs quote-card quote-one">
    <svg class="quote-mark" width="46" height="36" viewBox="0 0 46 36" aria-hidden="true"><path d="M0 0H19V20L10 36H3L8 20H0Z M25 0H44V20L35 36H28L33 20H25Z" fill="#0054AA"/></svg>
    <p class="quote-text">“You bare your heart and share things you wouldn’t under normal circumstances. You get to know each other very quickly. There’s that sort of intense, shared experience that comes from speaking to each other’s lives.”</p>
    <p class="quote-name">Sarah, Medical Director</p>
    <div class="cta-block">Secure your spot now<br>and ignite your<br>leadership potential</div>
  </div>

  <div class="abs date-bar">7 FEBRUARY 2024 – 11 DECEMBER 2024</div>
  <div class="abs time-bar">TIME: 7:30AM – 8:45AM (UK TIME)</div>

  <div class="abs details">
    <span class="label" style="width:104px">Commitment</span>: Wednesdays, every 2 weeks<br>
    <span class="label" style="width:112px">Location</span>: Connect from anywhere by VideoLink<br>
    <span class="label">Cost:</span> £3350 [UK] €3900 [Europe] A$6530 [Australia]<br>
    Payment options available
  </div>

  <div class="abs brand-mark brand-one">
    <span class="dot"></span>
    <span class="name">Marlow<br>Advisory</span>
  </div>
</section>

<section class="page page-two">
  <div class="abs top-band">Expertly guided by insight, academic rigour &amp; practical leadership strategies</div>

  <article class="abs bio-card bio-left">
    <div class="portrait-ring"><div class="portrait portrait-a" role="img" aria-label="Portrait photograph of Prof. Daniel Marsh"></div></div>
    <h3 class="bio-name serif">Prof. Daniel Marsh</h3>
    <p class="bio-text">Professor Daniel Marsh has 30 years’ experience developing leaders. An award-winning business school professor, group analyst and psychoanalytic psychotherapist, he has taught senior leadership programmes at Westbridge University, Thameside College London and Southbank University. His extensive leadership experience as a national health service clinical director and consultant psychotherapist inform his work as a GCA accredited executive coach. With a PhD from Kingsway College, University of Northfield, he is an expert in melding psychological insights with strategic organisational change.</p>
  </article>

  <article class="abs bio-card bio-right">
    <div class="portrait-ring"><div class="portrait portrait-b" role="img" aria-label="Portrait photograph of Dr. Helen Ashby"></div></div>
    <h3 class="bio-name serif">Dr. Helen Ashby</h3>
    <p class="bio-text">Dr Helen Ashby is a renowned psychoanalyst, group analyst, consultant psychiatrist and organisational consultant in the health sector. She has 20 years of leadership within the national health service, and she was also the National Director of Therapies for the Harbourview Group, directing therapy services across 100 UK hospitals. She holds prominent positions as Chair of the Patient Safety Group, Chair of the Working Group on the Effect of Suicide and Homicide on Psychiatrists, and Vice Chair of the Psychotherapy Faculty at the Royal Society of Psychiatric Medicine.</p>
  </article>

  <div class="abs explore">
    Engage with global leaders, gain diverse insights and forge lasting bonds. Explore questions such as:
    <ul>
      <li>What kind of leader do I aspire to be in the next chapter of my life and career?</li>
      <li>unique qualities and actions do I offer that no one else can?</li>
      <li>How can I galvanise my personal strengths to inspire and motivate others?</li>
    </ul>
  </div>

  <div class="abs spots">
    <div class="tag">Limited spots available</div>
    <p class="pitch">Don’t miss this unique<br>opportunity to transform your<br>leadership journey.</p>
  </div>

  <div class="abs quote-card quote-two">
    <svg class="quote-mark" width="46" height="36" viewBox="0 0 46 36" aria-hidden="true"><path d="M0 0H19V20L10 36H3L8 20H0Z M25 0H44V20L35 36H28L33 20H25Z" fill="#0054AA"/></svg>
    <p class="quote-text">“Through this exceptional coaching, our leadership team elevated its performance to lead the hospital with greater clarity, cohesion and thoughtfulness. Not only do we provide a superior work environment for staff, but better care for our patients.”</p>
    <p class="quote-name">John, CEO</p>
  </div>

  <div class="abs brand-mark brand-two">
    <span class="dot"></span>
    <span class="name">Marlow<br>Advisory</span>
  </div>

  <div class="abs accreditations" aria-label="Professional accreditations">
    <span class="badge badge-round"></span>
    <span class="badge badge-square"></span>
    <span class="badge badge-square"></span>
    <span class="badge badge-square"></span>
  </div>

  <div class="abs footer">
    <svg class="footer-art" width="911" height="120" viewBox="0 0 911 120" aria-hidden="true">
      <polygon points="524,0 911,0 911,120 458,120" fill="#dfe9f6"/>
      <polygon points="0,0 393,0 458,120 0,120" fill="#0054AA"/>
    </svg>
  </div>
  <p class="abs footer-call serif">Book your FREE<br>discovery call</p>

  <div class="abs contacts">
    <div class="row">
      <svg width="15" height="11" viewBox="0 0 15 11" aria-hidden="true"><rect x="0.75" y="0.75" width="13.5" height="9.5" fill="none" stroke="#0054AA" stroke-width="1.3"/><path d="M1 1 L7.5 6 L14 1" fill="none" stroke="#0054AA" stroke-width="1.3"/></svg>
      daniel@marlowadvisory.com
    </div>
    <div class="row">
      <svg width="15" height="11" viewBox="0 0 15 11" aria-hidden="true"><rect x="0.75" y="0.75" width="13.5" height="9.5" fill="none" stroke="#0054AA" stroke-width="1.3"/><path d="M1 1 L7.5 6 L14 1" fill="none" stroke="#0054AA" stroke-width="1.3"/></svg>
      helenashby@mailbox.net
    </div>
    <div class="site">www.marlowadvisory.com</div>
  </div>
</section>

</body>
</html>
```